Real Estate Business Card

On the front side I want to have my info, my brokerage info.
On the back side I want have my complany’s logo, website and Facebook link. I will provide all this once I select a design.

I would like to see Black background and gold text, Dark Blue and gold text and White and blue text designs

Font styles to use
Sans Serif
Script

```html
<!DOCTYPE html>
<html lang="en">
<head>
<meta charset="utf-8">
<title>Stoneway Real Estate – Business Card</title>
<link href="https://fonts.googleapis.com/css2?family=Great+Vibes&family=Work+Sans:wght@400;500;700;800&display=swap" rel="stylesheet">
<style>
  :root {
    --backdrop: #222222;
    --card: #141414;
    --card-edge: #1e1e1e;
    --gold: #d4af5f;
    --gold-soft: #e6cf95;
    --divider: #d4af5f;
    --badge: #f4f1ea;
  }
  * { margin: 0; padding: 0; box-sizing: border-box; }
  html, body {
    width: 1200px; height: 900px; overflow: hidden;
    background: var(--backdrop);
    font-family: "Work Sans", Arial, sans-serif;
    color: var(--gold-soft);
  }
  .canvas { position: relative; width: 1200px; height: 900px; }
  .card {
    position: absolute; width: 700px; height: 400px;
    background: linear-gradient(135deg, var(--card) 0%, var(--card-edge) 100%);
    box-shadow: 0 12px 30px rgba(0,0,0,.55);
    overflow: hidden;
  }
  .card--back { left: 320px; top: 40px; }
  .card--front { left: 180px; top: 465px; }

  .brand { position: absolute; display: flex; align-items: center; gap: 16px; color: var(--gold); font-weight: 800; }
  .brand__square { width: 46px; height: 46px; background: var(--gold); flex: none; }
  .brand__name { font-size: 44px; line-height: 1; letter-spacing: 1px; text-transform: uppercase; }
  .brand__name span { display: block; font-size: 17px; letter-spacing: 8px; margin-top: 8px; }
  .card--back .brand { left: 50%; top: 50%; transform: translate(-50%, -50%); }
  .card--front .brand { left: 45px; top: 150px; }
  .card--front .brand__name { font-size: 38px; }
  .card--front .brand__name span { font-size: 15px; letter-spacing: 6px; }

  .divider { position: absolute; left: 392px; top: 40px; width: 2px; height: 200px; background: var(--divider); }

  .details { position: absolute; left: 415px; top: 36px; width: 270px; }
  .details__name { font-family: "Great Vibes", cursive; color: var(--gold); font-size: 42px; font-weight: 400; line-height: 1; }
  .details__role { font-size: 15px; margin-top: 2px; letter-spacing: 1px; text-transform: uppercase; color: var(--gold); }
  .details__address { font-size: 15px; line-height: 1.4; margin-top: 14px; }
  .contact { list-style: none; margin-top: 12px; font-size: 15px; line-height: 1.5; }
  .contact li { display: flex; align-items: center; gap: 8px; }
  .contact svg { width: 11px; height: 11px; flex: none; }
  .contact .domain { color: var(--gold); font-weight: 500; }

  .badges { position: absolute; left: 415px; top: 300px; display: flex; gap: 12px; }
  .badge { background: var(--badge); }
  .badge--broker { width: 130px; height: 46px; }
  .badge--award { width: 110px; height: 46px; }
</style>
</head>
<body>
<main class="canvas">

  <section class="card card--back" aria-label="Card back">
    <div class="brand">
      <div class="brand__square"></div>
      <div class="brand__name">Stoneway<span>Real Estate</span></div>
    </div>
  </section>

  <section class="card card--front" aria-label="Card front">
    <div class="brand">
      <div class="brand__square"></div>
      <div class="brand__name">Stoneway<span>Real Estate</span></div>
    </div>

    <div class="divider"></div>

    <div class="details">
      <p class="details__name">Daniel Reyes</p>
      <p class="details__role">Director</p>
      <p class="details__address">1580 Harbor Ave #310<br>Calgary, Alberta T3K 4P1</p>
      <ul class="contact">
        <li>
          <svg viewBox="0 0 12 12" aria-hidden="true"><path d="M3 1 L5 3.5 L4 5 Q5 7.5 7 8 L8.5 7 L11 9 L9.5 11 Q3 10.5 1 2.5 Z" fill="var(--gold)"/></svg>
          +1 555-014-2270
        </li>
        <li>
          <svg viewBox="0 0 12 12" aria-hidden="true"><rect x="1" y="2.5" width="10" height="7" fill="none" stroke="var(--gold)" stroke-width="1.3"/><path d="M1 2.5 L6 6.5 L11 2.5" fill="none" stroke="var(--gold)" stroke-width="1.3"/></svg>
          info@stonewayrealestate.com
        </li>
        <li>
          <svg viewBox="0 0 12 12" aria-hidden="true"><circle cx="6" cy="6" r="5" fill="none" stroke="var(--gold)" stroke-width="1.2"/><path d="M1 6 H11 M6 1 Q3 6 6 11 M6 1 Q9 6 6 11" fill="none" stroke="var(--gold)" stroke-width="1"/></svg>
          <span>www.<span class="domain">stonewayrealestate</span>.com</span>
        </li>
      </ul>
    </div>

    <div class="badges">
      <div class="badge badge--broker" role="img" aria-label="Brokerage partner badge"></div>
      <div class="badge badge--award" role="img" aria-label="Office award badge"></div>
    </div>
  </section>

</main>
</body>
</html>
```